Professional, modern and unique business card. We are looking to present a new look to our business cards however we don't want to divert too far away from original template. We want social media links and our 3 office addresses on the backside of the business cards. Please see attached business card templates for ideas.
Cobalt Homes Color Code:
R: 7
G:63
B:86

Target Market(s)

Real Estate

Industry/Entity Type

Real Estate

Contact Information for Business Card

Follow the attached templates. In need of a more modern and unique touch but don't want to divert from the original theme or color.
Cobalt Homes Color Code:
R: 7
G:63
B:86

Font styles to use
Serif

Requirements
Must have
• Cobalt Homes logo, Cobalt homes colors, social media links, 3 office addresses,
Nice to have
• information about Cobalt Homes and QR codes. You can check out www.mycobalthomesagent.com

```html
<!DOCTYPE html>
<html lang="en">
<head>
<meta charset="utf-8">
<title>Cobalt Homes – Business Card</title>
<link rel="stylesheet" href="https://fonts.googleapis.com/css2?family=Cinzel:wght@600;700&family=Lato:wght@400&display=swap">
<style>
  :root {
    --backdrop: #5d5d5d;
    --card-light: #ffffff;
    --card-dark: #121212;
    --ink: #111111;
    --ink-soft: #222222;
    --on-dark: #e6e6e6;
    --brand-tint: #cfe7ef;
    --divider-light: #d8d8d8;
    --divider-dark: #555555;
    --icon: #3d7f9c;
  }
  * { margin: 0; padding: 0; box-sizing: border-box; }
  html, body { width: 1200px; height: 802px; overflow: hidden; }
  body { background: var(--backdrop); position: relative; font-family: "Lato", sans-serif; }

  .card { position: absolute; top: 274px; width: 443px; height: 265px; box-shadow: 0 3px 8px rgba(0,0,0,.45); }
  .card--front { left: 136px; background: var(--card-light); color: var(--ink); }
  .card--back { left: 624px; background: var(--card-dark); color: var(--on-dark); }

  .wordmark { position: absolute; left: 117px; top: 132px; transform: translate(-50%, -50%); text-align: center; font-family: "Cinzel", serif; font-weight: 700; }
  .wordmark__name { font-size: 33px; letter-spacing: 1px; line-height: 1; }
  .wordmark__sub { font-size: 12px; letter-spacing: 17px; margin-top: 10px; margin-right: -17px; line-height: 1; }
  .card--front .wordmark { color: var(--ink); }
  .card--back .wordmark { color: var(--brand-tint); }

  .divider { position: absolute; left: 218px; width: 1px; top: 66px; height: 134px; }
  .card--front .divider { background: var(--divider-light); }
  .card--back .divider { background: var(--divider-dark); top: 78px; height: 108px; }

  .person { position: absolute; left: 236px; top: 70px; }
  .person__name { font-family: "Cinzel", serif; font-weight: 700; font-size: 19px; line-height: 1; }
  .person__title { font-size: 12.5px; margin-top: 3px; letter-spacing: .2px; }

  .contacts { position: absolute; left: 236px; top: 122px; list-style: none; font-size: 12.5px; color: var(--ink-soft); }
  .contacts li { display: flex; align-items: center; height: 14.8px; }
  .contacts svg { width: 9px; height: 9px; margin-right: 5px; fill: var(--ink); flex: none; }

  .socials { position: absolute; left: 234px; top: 77px; list-style: none; font-size: 13px; }
  .socials li { display: flex; align-items: center; height: 18.6px; }
  .socials .dot { width: 15px; height: 15px; border-radius: 50%; background: var(--icon); margin-right: 5px; flex: none; }

  .offices { position: absolute; left: 0; right: 0; top: 212px; display: flex; justify-content: center; font-size: 12.5px; line-height: 15px; }
  .office { text-align: center; padding: 0 7px; }
  .office + .office { border-left: 1px solid #888; }
</style>
</head>
<body>
  <section class="card card--front" aria-label="Business card front">
    <div class="wordmark">
      <div class="wordmark__name">COBALT</div>
      <div class="wordmark__sub">HOMES</div>
    </div>
    <div class="divider"></div>
    <div class="person">
      <div class="person__name">DANA WHITFIELD</div>
      <div class="person__title">MANAGING DIRECTOR</div>
    </div>
    <ul class="contacts">
      <li><svg viewBox="0 0 10 10"><path d="M1 3c0-1 1-2 4-2s4 1 4 2v1H7V3H3v1H1zM2 5h6l1 4H1z"/></svg>212 555 0147</li>
      <li><svg viewBox="0 0 10 10"><path d="M3 0h4a1 1 0 0 1 1 1v8a1 1 0 0 1-1 1H3a1 1 0 0 1-1-1V1a1 1 0 0 1 1-1zm0 1.5v6h4v-6z"/></svg>917 555 0182</li>
      <li><svg viewBox="0 0 10 10"><path d="M3 0h4v3H3zM1 3.5h8v4H8V10H2V7.5H1zm2 3v2.5h4V6.5z"/></svg>212 555 0199</li>
      <li><svg viewBox="0 0 10 10"><path d="M0 2h10v6H0zm1 1v.3l4 2.5 4-2.5V3z"/></svg>info@cobalthomes.com</li>
      <li><svg viewBox="0 0 10 10"><circle cx="5" cy="5" r="4.5"/></svg>www.mycobalthomesagent.com</li>
    </ul>
  </section>

  <section class="card card--back" aria-label="Business card back">
    <div class="wordmark">
      <div class="wordmark__name">COBALT</div>
      <div class="wordmark__sub">HOMES</div>
    </div>
    <div class="divider"></div>
    <ul class="socials">
      <li><span class="dot"></span>CobalthomesNY</li>
      <li><span class="dot"></span>Info at Cobalt Homes</li>
      <li><span class="dot"></span>Cobalt Homes New York</li>
      <li><span class="dot"></span>Cobalt Homes</li>
      <li><span class="dot"></span>@CobaltHomesQ</li>
      <li><span class="dot"></span>@CobaltHomesNY</li>
    </ul>
    <div class="offices">
      <div class="office">148-10 Harbor Blvd<br>Bayside, NY 11360</div>
      <div class="office">72-30 Maple Ave<br>Forest Hills, NY 11375</div>
      <div class="office">905 Orchard St<br>Brooklyn, NY 11207</div>
    </div>
  </section>
</body>
</html>
```